Plakat-Design für Schwarz-Weiß-Ball
Zielgruppe
Parteipolitische Organisatoin BVL
Aufgabenstellung
Plakat für einen Schwarz-Weißball in A1 und A6. Für den A6 Flyer müsste man den Zusatz aufnehmen Für alle Haushalte mit Tagespost.
Datum 01.02.2020
Ort Gasthof Lindenkrug Allershausen
Live mit der Band Morgentau
Kartenpreis 16,00 € Vorverkauf
18,00 € Abendkasse
inkl. Sektemfapng und Begrüßungsgeschenk für die Damen
Einalass 19:00 Uhr Beginn 20,00 Uhr
Reservierung GAsthof Lindenkrug 08162 / 473820
V.i.s. d.P. BVL Allershausen, Tobias Rehberg, Ahornweg 14 ,85417 Allershausen
Eigentlich werden keine Bilder benötigt.

```html
<!DOCTYPE html>
<html lang="de">
<head>
<meta charset="utf-8">
<title>Schwarz-Weißball – Plakat</title>
<link rel="stylesheet" href="https://fonts.googleapis.com/css2?family=Exo+2:wght@700;800;900&family=Fira+Sans:wght@400;500;700;800&display=swap">
<style>
  :root {
    --night: #0f1a21;
    --gold: #cfba85;
    --gold-text: #c9b27c;
    --bronze: #8b6a3c;
    --ink: #1b2026;
    --paper: #ffffff;
  }
  * { margin: 0; padding: 0; box-sizing: border-box; }
  html, body { width: 914px; height: 1200px; overflow: hidden; background: var(--paper); }
  .poster {
    position: relative;
    width: 914px;
    height: 1200px;
    background: var(--paper);
    font-family: "Fira Sans", sans-serif;
    color: var(--ink);
    overflow: hidden;
  }
  .backdrop { position: absolute; inset: 0; }
  .headline {
    position: absolute;
    left: 58px;
    top: 222px;
    font-family: "Exo 2", sans-serif;
    font-weight: 900;
    font-size: 147px;
    line-height: 132px;
    color: var(--paper);
    letter-spacing: 1px;
  }
  .event-when {
    position: absolute;
    left: 60px;
    top: 518px;
    font-family: "Exo 2", sans-serif;
    font-weight: 800;
    font-size: 80px;
    line-height: 1;
  }
  .event-date { color: var(--gold-text); }
  .event-time { color: var(--paper); margin-left: 40px; }
  .venue {
    position: absolute;
    left: 61px;
    top: 610px;
    font-size: 37px;
    font-weight: 400;
    color: var(--gold-text);
  }
  .band-intro {
    position: absolute;
    left: 61px;
    top: 709px;
    font-size: 29px;
    font-weight: 800;
    letter-spacing: 0.5px;
  }
  .band-name {
    position: absolute;
    left: 58px;
    top: 742px;
    font-family: "Exo 2", sans-serif;
    font-size: 74px;
    font-weight: 800;
    line-height: 1;
  }
  .price-label {
    position: absolute;
    left: 61px;
    top: 834px;
    font-size: 32px;
    font-weight: 400;
    letter-spacing: 1px;
  }
  .prices {
    position: absolute;
    left: 61px;
    top: 868px;
    display: flex;
    gap: 30px;
    font-size: 46px;
    font-weight: 700;
  }
  .price { display: flex; align-items: center; gap: 12px; }
  .price::before {
    content: "";
    width: 11px; height: 11px;
    background: var(--bronze);
    transform: rotate(45deg);
  }
  .price-note {
    position: absolute;
    left: 61px;
    top: 929px;
    font-size: 21px;
    font-weight: 500;
    letter-spacing: 1.6px;
  }
  .doors {
    position: absolute;
    left: 61px;
    top: 993px;
    font-size: 37px;
    color: var(--bronze);
  }
  .reservation-label {
    position: absolute;
    left: 61px;
    top: 1078px;
    font-size: 33px;
    font-weight: 800;
    letter-spacing: 0.5px;
  }
  .reservation-line {
    position: absolute;
    left: 61px;
    top: 1118px;
    font-size: 44px;
    font-weight: 800;
    white-space: nowrap;
    letter-spacing: 0.5px;
  }
  .reservation-venue { color: var(--bronze); }
  .organiser {
    position: absolute;
    right: 48px;
    top: 1004px;
    text-align: right;
    font-family: "Fira Sans", sans-serif;
    font-weight: 700;
    font-size: 32px;
    line-height: 40px;
    color: var(--ink);
  }
</style>
</head>
<body>
<main class="poster">
  <svg class="backdrop" width="914" height="1200" viewBox="0 0 914 1200" aria-hidden="true">
    <rect class="night-field" x="0" y="0" width="914" height="760" fill="var(--night)"/>
    <path class="gold-band" d="M0 700 C 180 672, 420 688, 600 716 C 720 736, 820 744, 914 728 L914 980 L0 980 Z" fill="var(--gold)"/>
    <path class="wave wave-upper" d="M0 40 C 150 20, 300 60, 400 95 C 460 115, 520 115, 555 70 C 520 140, 430 150, 340 125 C 230 95, 120 70, 0 85 Z" fill="#ffffff" opacity="0.13"/>
    <path class="wave wave-lower" d="M0 130 C 140 100, 300 150, 440 205 C 560 250, 680 255, 760 125 C 700 250, 600 300, 470 270 C 320 235, 160 165, 0 180 Z" fill="#cfba85" opacity="0.12"/>
  </svg>

  <svg width="914" height="1200" viewBox="0 0 914 1200" style="position:absolute;inset:0">
    <defs>
      <linearGradient id="dancer-tone" x1="0" y1="0" x2="0" y2="1">
        <stop offset="0" stop-color="#ffffff" stop-opacity="0.85"/>
        <stop offset="1" stop-color="#ffffff" stop-opacity="0.6"/>
      </linearGradient>
    </defs>
    <rect class="dancers" x="580" y="42" width="140" height="200" rx="24" fill="url(#dancer-tone)" role="img" aria-label="Weiße Silhouette eines tanzenden Paares"/>
    <rect class="music-notes" x="722" y="548" width="150" height="200" rx="24" fill="var(--gold)" opacity="0.3" role="img" aria-label="Goldene Musiknoten"/>
  </svg>

  <h1 class="headline">SCHWARZ-<br>WEIßBALL</h1>

  <p class="event-when"><span class="event-date">01.02.2020</span><span class="event-time">20:00</span></p>
  <p class="venue">Gasthof Lindenkrug Allershausen</p>

  <p class="band-intro">LIVE MIT DER</p>
  <p class="band-name">BAND MORGENTAU</p>

  <p class="price-label">KARTENPREIS</p>
  <div class="prices">
    <span class="price">16,00 € VVK</span>
    <span class="price">18,00 € AK</span>
  </div>
  <p class="price-note">INKL. SEKTEMFAPNG UND BEGRÜßUNGSGESCHENK FÜR DIE DAMEN</p>

  <p class="doors">Einlass 19:00 Uhr</p>
  <p class="reservation-label">RESERVIERUNG:</p>
  <p class="reservation-line"><span class="reservation-venue">GASTHOF LINDENKRUG</span> 08162 / 473820</p>

  <p class="organiser">BVL<br>Ortsverband Allershausen</p>
</main>
</body>
</html>
```